IT COMPANYcutting edge tec business card

we are IT company that building any apps.
we need business card in japanese and english
You don’t have to include all information in front one you can attach part of that information to back-side
company name : 株式会社ひかりの丘 (BRIGHTHILL Inc.)
concept : cutting-edge technology
role : 取締役 (director)
name : 呉 炫秀 (Oh Hyeonsuk)
post number : 154-0038
address : 東京都世田谷区西若葉台5-14-8 (5-14-8, Nishiwakabadai, Setagaya Ku, Tokyo To, 154-0038, Japan)
Tel:+81-3-5917-2846
Mobile:+81-80-7253-3169
Email : hoh@brighthill-lab.com
website : www.brighthill-lab.com

we dont have logo so please make it as well
we also looking for designer who can make homapage design.

Contact Information for Business Card

cutting-edge design and modern for IT

Font styles to use
Sans Serif

Colors
34a6d7
33b8a4
6092c4
3377b5
886aae
6b449b
b868aa
a64599

Requirements
Must have
• Simple but designed

```html
<!DOCTYPE html>
<html lang="ja">
<head>
<meta charset="utf-8">
<title>BRIGHTHILL Inc. – Business Card</title>
<link rel="stylesheet" href="https://fonts.googleapis.com/css2?family=Ubuntu:wght@400;500&family=Noto+Sans+JP:wght@300;400&display=swap">
<style>
  :root {
    --page-bg: #e6e6e6;
    --card-bg: #ffffff;
    --shadow: #5a5a5a;
    --accent-purple: #9a34e6;
    --accent-mint: #55f79a;
    --name-mint: #45ec8f;
    --on-band: #ffffff;
  }
  html, body {
    margin: 0;
    padding: 0;
    width: 887px;
    height: 1200px;
    overflow: hidden;
    background: var(--page-bg);
  }
  .business-card {
    position: absolute;
    left: 43px;
    top: 355px;
    width: 800px;
    height: 489px;
    background: var(--card-bg);
    box-shadow: 8px 8px 0 var(--shadow);
    font-family: "Ubuntu", "Noto Sans JP", sans-serif;
    color: var(--accent-purple);
    overflow: hidden;
  }
  .address-block {
    position: absolute;
    left: 35px;
    top: 24px;
    font-size: 18px;
    line-height: 23.5px;
    font-weight: 500;
  }
  .address-block p { margin: 0; }
  .identity-block {
    position: absolute;
    right: 36px;
    top: 34px;
    text-align: right;
    color: var(--name-mint);
    font-weight: 500;
  }
  .identity-block p { margin: 0; }
  .name-ja { font-family: "Noto Sans JP", sans-serif; font-weight: 400; font-size: 29px; line-height: 34px; letter-spacing: 2px; }
  .name-en { font-size: 32px; line-height: 36px; letter-spacing: 0.5px; }
  .role-ja { font-family: "Noto Sans JP", sans-serif; font-weight: 400; font-size: 22px; line-height: 26px; margin-top: 10px !important; }
  .role-en { font-size: 22px; line-height: 24px; }
  .identity-rule {
    position: absolute;
    right: 36px;
    top: 171px;
    width: 230px;
    height: 2px;
    background: var(--accent-purple);
  }
  .contact-list {
    position: absolute;
    right: 36px;
    top: 192px;
    margin: 0;
    padding: 0;
    list-style: none;
    text-align: right;
    font-size: 22px;
    line-height: 33.5px;
    font-weight: 500;
  }
  .brand-band {
    position: absolute;
    left: 0;
    top: 301px;
    width: 800px;
    height: 188px;
    background: var(--accent-mint);
  }
  .brand-dot {
    position: absolute;
    left: 42px;
    top: 28px;
    width: 68px;
    height: 68px;
    border-radius: 50%;
    background: var(--accent-purple);
  }
  .brand-name {
    position: absolute;
    left: 141px;
    top: 36px;
    font-family: "Noto Sans JP", sans-serif;
    font-weight: 300;
    color: var(--on-band);
    margin: 0;
  }
  .brand-name-ja { display: block; font-size: 40px; line-height: 48px; letter-spacing: 1px; }
  .brand-name-en { display: block; font-size: 42px; line-height: 50px; letter-spacing: -1.5px; }
  .band-rule {
    position: absolute;
    top: 164px;
    width: 230px;
    height: 2px;
    background: var(--accent-purple);
  }
  .band-rule.left { left: 35px; }
  .band-rule.right { right: 36px; }
  .website {
    position: absolute;
    left: 0;
    right: 0;
    top: 152px;
    text-align: center;
    font-size: 19px;
    line-height: 24px;
    font-weight: 500;
    color: var(--accent-purple);
  }
</style>
</head>
<body>
  <section class="business-card">
    <div class="address-block">
      <p>154-0038</p>
      <p>東京都世田谷区西若葉台5-14-8</p>
      <p>Address:</p>
      <p>5-14-8, Nishiwakabadai,</p>
      <p>Setagaya Ku, Tokyo To, 154-0038,</p>
      <p>Japan</p>
    </div>

    <div class="identity-block">
      <p class="name-ja">呉 炫秀</p>
      <p class="name-en">Oh Hyeonsuk</p>
      <p class="role-ja">取締役</p>
      <p class="role-en">Director</p>
    </div>
    <div class="identity-rule"></div>

    <ul class="contact-list">
      <li>Mobile: +81-80-7253-3169</li>
      <li>Phone: +81-3-5917-2846</li>
      <li>E-mail: hoh@brighthill-lab.com</li>
    </ul>

    <div class="brand-band">
      <div class="brand-dot"></div>
      <p class="brand-name">
        <span class="brand-name-ja">株式会社ひかりの丘</span>
        <span class="brand-name-en">BRIGHTHILL Inc.</span>
      </p>
      <div class="band-rule left"></div>
      <div class="website">www.brighthill-lab.com</div>
      <div class="band-rule right"></div>
    </div>
  </section>
</body>
</html>
```